KORVELTA Corporate Business Card

Modern business card design for company which focuses in the areas of Staffing, IT Consulting & Data Services. Please note: We are no longer using the IT subscript on the logo. All designs should have IT subscript removed.
Website: www.korveltait.example

```html
<!DOCTYPE html>
<html lang="en">
<head>
<meta charset="utf-8">
<title>KORVELTA Business Card</title>
<link href="https://fonts.googleapis.com/css2?family=Lato:wght@400;700&family=Michroma&display=swap" rel="stylesheet">
<style>
  :root {
    --page: #2b2c30;
    --card-dark: #0a0c10;
    --card-ink: #05070a;
    --blue-bright: #1f9fe0;
    --blue-deep: #0b6aa8;
    --text-light: #e6eef5;
    --tile: #121820;
  }
  html, body {
    margin: 0;
    width: 1200px;
    height: 900px;
    overflow: hidden;
    background: var(--page);
  }
  .canvas {
    position: relative;
    width: 1200px;
    height: 900px;
  }
  .card {
    position: absolute;
    width: 560px;
    height: 320px;
    overflow: hidden;
    background: var(--card-dark);
    box-shadow: 0 12px 30px rgba(0,0,0,.45);
  }
  .card--back  { left: 580px; top: 90px; }
  .card--front { left: 60px; top: 470px; }

  .front-tiles {
    position: absolute;
    left: 0; top: 0;
    width: 380px; height: 170px;
    background: radial-gradient(ellipse at 45% 45%, var(--tile) 0%, var(--card-dark) 75%);
  }
  .front-waves {
    position: absolute;
    inset: 0;
  }
  .brand-name {
    position: absolute;
    right: 36px;
    top: 62px;
    margin: 0;
    font-family: "Michroma", sans-serif;
    font-size: 38px;
    letter-spacing: 1px;
    color: var(--blue-bright);
    line-height: 1;
  }
  .contact {
    position: absolute;
    right: 30px;
    top: 168px;
    text-align: right;
    font-family: "Lato", sans-serif;
    color: var(--text-light);
    font-size: 15px;
    line-height: 20px;
  }
  .contact p { margin: 0; }
  .contact__name {
    font-weight: 700;
    font-size: 16px;
    letter-spacing: 1px;
    color: #4cc0f5;
  }
  .contact__line--icon {
    display: flex;
    justify-content: flex-end;
    align-items: center;
    gap: 7px;
  }
  .contact__icon { width: 13px; height: 13px; flex: none; }

  .back-pattern {
    position: absolute;
    inset: 0;
    background: linear-gradient(135deg, #111419, var(--card-ink));
  }
  .back-mark {
    position: absolute;
    right: 70px;
    bottom: 70px;
    display: flex;
    align-items: center;
    gap: 10px;
    font-family: "Michroma", sans-serif;
    font-size: 20px;
    letter-spacing: 1px;
    color: var(--blue-bright);
  }
  .back-mark__square {
    width: 22px;
    height: 22px;
    border: 3px solid var(--blue-bright);
    border-radius: 4px;
    box-sizing: border-box;
  }
</style>
</head>
<body>
<main class="canvas">

  <section class="card card--back">
    <div class="back-pattern" role="img" aria-label="Faint repeating brand pattern on black"></div>
    <div class="back-mark">
      <span class="back-mark__square"></span>
      <span>KORVELTA</span>
    </div>
  </section>

  <section class="card card--front">
    <div class="front-tiles" role="img" aria-label="Faint dark tile pattern"></div>
    <svg class="front-waves" width="560" height="320" viewBox="0 0 560 320" aria-hidden="true">
      <path d="M0 112 C 110 116, 230 150, 330 168 C 230 158, 110 128, 0 126 Z" fill="var(--blue-bright)"/>
      <path d="M0 140 C 180 150, 380 180, 560 100 L560 320 L0 320 Z" fill="var(--blue-bright)"/>
      <path d="M0 152 C 180 162, 380 194, 560 116 L560 320 L0 320 Z" fill="var(--blue-deep)"/>
    </svg>

    <h1 class="brand-name">KORVELTA</h1>

    <div class="contact">
      <p class="contact__name">DANIEL OKAFOR</p>
      <p>Sales Manager</p>
      <p>418 Harlow Ave</p>
      <p>Brenton, IN 47000</p>
      <p class="contact__line--icon">555-014-2290
        <svg class="contact__icon" viewBox="0 0 16 16" aria-hidden="true"><circle cx="8" cy="8" r="7" fill="none" stroke="var(--blue-bright)" stroke-width="1.5"/><path d="M5.5 4.5 L7 6 L6.2 7.2 C6.8 8.4 7.6 9.2 8.8 9.8 L10 9 L11.5 10.5 L10.6 11.6 C7.6 11 5 8.4 4.4 5.4 Z" fill="var(--blue-bright)"/></svg>
      </p>
      <p class="contact__line--icon">contactus@korveltait.example
        <svg class="contact__icon" viewBox="0 0 16 16" aria-hidden="true"><rect x="1.5" y="3.5" width="13" height="9" fill="none" stroke="var(--blue-bright)" stroke-width="1.5"/><path d="M1.5 3.5 L8 9 L14.5 3.5" fill="none" stroke="var(--blue-bright)" stroke-width="1.5"/></svg>
      </p>
      <p class="contact__line--icon">www.korveltait.example
        <svg class="contact__icon" viewBox="0 0 16 16" aria-hidden="true"><circle cx="8" cy="8" r="6.5" fill="none" stroke="var(--blue-bright)" stroke-width="1.5"/><ellipse cx="8" cy="8" rx="2.8" ry="6.5" fill="none" stroke="var(--blue-bright)" stroke-width="1.2"/><path d="M1.5 8 H14.5" stroke="var(--blue-bright)" stroke-width="1.2"/></svg>
      </p>
    </div>
  </section>

</main>
</body>
</html>
```